Homepage Real Estate Agency

I need a web design for a real estate agency in Luxembourg. A short draft for the front page can be found in the project details. (Page 1+2) The main colors of the site should be blue as shown in the project details. (Page 3)
The main target for this site is to promote real estates and a small presentation of the company.

Industry/Entity Type

Real Estate

Requirements
Must have
• On the front page estates are shown in a short preview in small boxes, on the right side is a search. The search is hidden except for the front page. The header has 4 buttons and the logo of the company.

```html
<!DOCTYPE html>
<html lang="fr">
<head>
<meta charset="utf-8">
<title>Maison Lumen – Immobilier</title>
<link rel="stylesheet" href="https://fonts.googleapis.com/css2?family=Arimo:wght@400;700&family=Oswald:wght@400;500&family=Source+Sans+3:wght@600;700&display=swap">
<style>
:root{
  --blue:#062d96;
  --blue-deep:#04247c;
  --red:#c8261a;
  --red-btn:#c0301c;
  --paper:#efeeec;
  --card:#e9e8e7;
  --card-inner:#e2e1e1;
  --line:#9b9b9b;
  --field:#e3e3e3;
  --muted:#8a8a8a;
  --ink:#222;
  --footer:#a9a9a9;
}
*{box-sizing:border-box;margin:0;padding:0}
html,body{width:942px;height:1200px;overflow:hidden}
body{position:relative;background:var(--paper);font-family:"Arimo",Arial,sans-serif;color:var(--ink)}
.abs{position:absolute}

.site-header{position:absolute;left:0;top:0;width:942px;height:426px;background:linear-gradient(var(--blue),var(--blue-deep))}
.header-rule{position:absolute;left:0;top:94px;width:942px;height:6px;background:linear-gradient(#e03a2e,#a8170f)}
.brand{position:absolute;left:166px;top:36px;display:flex;align-items:center;gap:8px;font-family:"Source Sans 3",sans-serif;font-weight:700;font-size:20px;color:#fff}
.brand-dot{width:12px;height:12px;border-radius:50%;background:#fff}
.main-nav{position:absolute;left:521px;top:71px;display:flex;gap:5px}
.main-nav a{display:block;width:61px;height:21px;line-height:21px;text-align:center;font-family:"Arimo",sans-serif;font-size:7.5px;font-weight:700;color:var(--red);text-decoration:none;background:linear-gradient(#fff,#dcdcdc);border:1px solid #bbb;border-radius:3px 3px 0 0}

.slider{position:absolute;left:155px;top:105px;width:632px;height:274px;background:linear-gradient(#f5f5f5,#dedede);border-radius:8px;box-shadow:0 14px 18px -10px rgba(0,0,0,.45)}
.slide-photo{position:absolute;left:13px;top:13px;width:606px;height:240px;background:linear-gradient(#9cbad6 0%,#c9d2c4 30%,#aab4a8 55%,#5f7c47 85%,#3f5a2e 100%)}
.slider-arrow{position:absolute;top:126px;width:34px;height:22px;background:linear-gradient(#fff,#d8d8d8);border:1px solid #bbb;border-radius:3px}
.slider-arrow span{position:absolute;top:5px;left:11px;width:11px;height:11px;border-radius:50%;border:2px solid #ccc}
.arrow-prev{left:-10px}.arrow-prev span{background:#888}
.arrow-next{right:-10px}.arrow-next span{background:var(--red)}
.slider-dots{position:absolute;left:293px;top:261px;display:flex;gap:8px}
.slider-dots i{width:6px;height:6px;border-radius:50%;background:#ccc}
.slider-dots i.on{background:var(--red)}

.rule-v{position:absolute;width:2px;background:var(--line);top:489px;height:552px}

.listing-title{position:absolute;font-family:"Source Sans 3",sans-serif;font-weight:700;font-size:22px;color:var(--blue);letter-spacing:.2px}
.listing{position:absolute;width:190px;height:250px}
.listing-photo-frame{position:absolute;left:0;top:0;width:190px;height:78px;background:#ebebeb;border:1px solid #d6d6d6;border-radius:3px}
.listing-photo{position:absolute;left:7px;top:6px;width:175px;height:63px}
.listing-body{position:absolute;left:7px;top:78px;width:176px;height:162px;background:var(--card);border:1px solid #dadada}
.listing-text{position:absolute;left:7px;top:0;width:162px;height:153px;background:var(--card-inner);border:1px solid #d4d4d4;padding:16px 10px 0 12px;font-size:8.3px;line-height:12.2px;color:#222}
.listing-text p+p{margin-top:12px}
.pin{position:absolute;left:86px;top:-3px;width:18px;height:10px;border-radius:0 0 9px 9px;background:var(--red);border:2px solid #fff;border-top:none}
.meta{position:absolute;left:12px;top:131px;font-size:5.5px;line-height:7px;color:#888}
.date{position:absolute;right:11px;top:124px;font-family:"Oswald",sans-serif;font-size:17px;color:#a5a5a5}
.read-more{position:absolute;left:65px;top:153px;width:56px;height:20px;line-height:18px;text-align:center;font-family:"Oswald",sans-serif;font-size:11px;color:var(--red-btn);background:linear-gradient(#fff,#e3e3e3);border:1px solid #aaa;border-radius:3px;text-decoration:none}

.search-title{position:absolute;left:662px;top:482px;font-family:"Source Sans 3",sans-serif;font-weight:700;font-size:22px;color:var(--blue)}
.search-label{position:absolute;left:660px;font-size:8.5px;color:#777}
.search-field{position:absolute;left:711px;width:144px;height:19px;background:var(--field);border:1px solid #d0d0d0}
.radio{position:absolute;left:712px;display:flex;align-items:center;gap:11px;font-size:8.5px;color:#777}
.radio i{width:11px;height:11px;border-radius:50%;background:#e6e6e6;border:1px solid #d2d2d2;position:relative}
.radio i.on::after{content:"";position:absolute;left:3px;top:3px;width:4px;height:4px;border-radius:50%;background:#333}
.search-btn{position:absolute;left:714px;top:731px;width:52px;height:17px;line-height:16px;text-align:center;font-size:8.5px;color:#777;background:#e2e2e2;border:1px solid #cfcfcf;border-radius:9px}

.site-footer{position:absolute;left:0;top:1146px;width:942px;height:54px;background:var(--footer)}
.footer-legal{position:absolute;left:157px;top:26px;font-size:8px;font-weight:700;color:#fff}
.footer-contact{position:absolute;left:803px;top:19px;font-size:12px;color:#fff}
</style>
</head>
<body>
<header class="site-header">
  <div class="header-rule"></div>
  <div class="brand"><span class="brand-dot"></span>Maison Lumen</div>
  <nav class="main-nav">
    <a href="#">A VENDRE</a><a href="#">CONSTRUCTION</a><a href="#">LOCATION</a><a href="#">CHERCHONS</a>
  </nav>
  <div class="slider">
    <div class="slide-photo" role="img" aria-label="Grande maison familiale à deux étages avec jardin fleuri"></div>
    <div class="slider-arrow arrow-prev"><span></span></div>
    <div class="slider-arrow arrow-next"><span></span></div>
    <div class="slider-dots"><i></i><i></i><i></i><i class="on"></i></div>
  </div>
</header>

<main>
  <div class="rule-v" style="left:157px"></div>
  <div class="rule-v" style="left:623px"></div>

  <h2 class="listing-title" style="left:194px;top:466px">HEADING</h2>
  <h2 class="listing-title" style="left:416px;top:466px">HEADING</h2>
  <h2 class="listing-title" style="left:194px;top:770px">HEADING</h2>
  <h2 class="listing-title" style="left:416px;top:770px">HEADING</h2>

  <article class="listing" style="left:188px;top:495px">
    <div class="listing-photo-frame"><div class="listing-photo" role="img" aria-label="Maison en pierre et bardage sous ciel bleu" style="background:linear-gradient(#5b8fd0,#a6b7c4 55%,#6b8a4e)"></div></div>
    <div class="listing-body"><div class="listing-text"><span class="pin"></span>
      <p>Proin eget orci a nulla consequat hendrerit. Nunc non dictum quam. Nam sed est non est imperdiet faucibus a vitae mauris.</p>
      <p>Suspendisse tincidunt, nunc nec porttitor molestie, sapien sem convallis erat, at faucibus diam neque</p>
      <div class="meta">Posted by User 002<br>Categories: lorem , ipsum</div><div class="date">Mai 26</div>
      <a class="read-more" href="#">Read More</a></div></div>
  </article>

  <article class="listing" style="left:410px;top:495px">
    <div class="listing-photo-frame"><div class="listing-photo" role="img" aria-label="Maison de plain-pied en brique avec pelouse" style="background:linear-gradient(#cfe0ee,#8c7a68 50%,#5fa040)"></div></div>
    <div class="listing-body"><div class="listing-text"><span class="pin"></span>
      <p>Proin eget orci a nulla consequat hendrerit. Nunc non dictum quam. Nam sed est non est imperdiet faucibus a vitae mauris.</p>
      <p>Suspendisse tincidunt, nunc nec porttitor molestie, sapien sem convallis erat, at faucibus diam neque</p>
      <div class="meta">Posted by User 002<br>Categories: lorem , ipsum</div><div class="date">Mai 26</div>
      <a class="read-more" href="#">Read More</a></div></div>
  </article>

  <article class="listing" style="left:188px;top:799px">
    <div class="listing-photo-frame"><div class="listing-photo" role="img" aria-label="Maison de banlieue avec façade en pierre" style="background:linear-gradient(#3f7fd6,#9aa6a0 55%,#4f8a2e)"></div></div>
    <div class="listing-body"><div class="listing-text"><span class="pin"></span>
      <p>Proin eget orci a nulla consequat hendrerit. Nunc non dictum quam. Nam sed est non est imperdiet faucibus a vitae mauris.</p>
      <p>Suspendisse tincidunt, nunc nec porttitor molestie, sapien sem convallis erat, at faucibus diam neque</p>
      <div class="meta">Posted by User 002<br>Categories: lorem , ipsum</div><div class="date">Mai 26</div>
      <a class="read-more" href="#">Read More</a></div></div>
  </article>

  <article class="listing" style="left:410px;top:799px">
    <div class="listing-photo-frame"><div class="listing-photo" role="img" aria-label="Villa aux tuiles orange entourée d'arbres" style="background:linear-gradient(#3c6b2e,#d8642e 35%,#c9b089 65%,#7a2a2a)"></div></div>
    <div class="listing-body"><div class="listing-text"><span class="pin"></span>
      <p>Proin eget orci a nulla consequat hendrerit. Nunc non dictum quam. Nam sed est non est imperdiet faucibus a vitae mauris.</p>
      <p>Suspendisse tincidunt, nunc nec porttitor molestie, sapien sem convallis erat, at faucibus diam neque</p>
      <div class="meta">Posted by User 002<br>Categories: lorem , ipsum</div><div class="date">Mai 26</div>
      <a class="read-more" href="#">Read More</a></div></div>
  </article>

  <aside>
    <h2 class="search-title">SEARCH HOMES</h2>
    <span class="search-label" style="top:531px">Type</span><div class="search-field" style="top:528px"></div>
    <span class="search-label" style="top:564px">Purpose</span><div class="search-field" style="top:560px"></div>
    <span class="search-label" style="top:598px">Price</span><div class="search-field" style="top:595px"></div>
    <span class="search-label" style="top:632px">Location</span><div class="search-field" style="top:629px"></div>
    <div class="radio" style="top:663px"><i class="on"></i>Choice 01</div>
    <div class="radio" style="top:684px"><i></i>Choice 02</div>
    <div class="radio" style="top:705px"><i></i>Choice 03</div>
    <div class="search-btn">Search</div>
  </aside>
</main>

<footer class="site-footer">
  <div class="footer-legal">RealEstate (c) 2012| Privacy policy</div>
  <div class="footer-contact">Contact us</div>
</footer>
</body>
</html>
```